TLM Friendspace Page Cover Image

I am setting up a Friendspace company page for my new business called 'TimberLineMetrics'. We provide business owners, executives, and managers with valuable information via a comprehensive suite of employee assessment products to make better people decisions. Company tagline is Recruit Wisely - Grow Teams - Reach Goals. I need a attention grabbing, polished, professional cover graphic to be displayed on the top of the page that captures who we are and is a nice compliment to our logo which will appear in the smaller logo box. Company personality is contemporary, energetic, competent yet humble. Logo is attached. Please view our 3 minute overview video on YouTube to get a sense of who we are/what we do. https://www.videohostsample.com/watch?v=Qa7nRt2LmWz

Target Market(s)

My website is a B2B website. My ideal "sweet spot" client company employees approximately 200-300 employees, although my secondary products and service market will include companies above 200-300 employees to include select Meridian 400 companies. Target client roles within these companies include:
- Business Leaders - CEO's, Presidents, and General Managers
- Small & Mid-sized business owners
- Functional Leaders - CFOs, CIO, Sales/Marketing leaders, HR leaders
- Functional Specialists - Recruiting, Learning & Development, OD
- 1st and 2nd line managers
Our products and services can be used effectively across all industries, but if I had to pick the top 5 or 6 "target" industries or type of businesses that match extremely well to our products/services I'd say retail/consumer products, healthcare/human services, direct/outside sales (*e.g. car dealers, medical equipment sales, telemarketing, etc.), customer service call centers, hospitality, and banking.

Industry/Entity Type

Business

Font styles to use
Sans Serif

Requirements
Nice to have
• Don't want the graphic to be too busy or crowded. Photography and/or from scratch graphics can be used separately or in combination. Attached is a sample from an unrelated web page I like in terms of it's white space/graphic/text balance.

```html
<!DOCTYPE html>
<html lang="en">
<head>
<meta charset="utf-8">
<title>TimberLineMetrics – Page Cover</title>
<link rel="stylesheet" href="https://fonts.googleapis.com/css2?family=Source+Sans+3:wght@400;600;700&display=swap">
<style>
:root{
  --page-bg:#e9ebf2;
  --bar-top:#5a74ab;
  --bar-bottom:#3f5b97;
  --bar-text:#dfe5f2;
  --card:#ffffff;
  --card-line:#c9cedb;
  --panel:#f2f3f8;
  --link:#3b5998;
  --muted:#6f7482;
  --ink:#1d2129;
  --tile:#7b7b7b;
  --tile-num:#a3a3a3;
  --accent:#1ab0f0;
  --rail:#c6cde0;
  --rail-active:#5b6fa3;
  --brand:#23276b;
}
*{box-sizing:border-box;margin:0;padding:0}
html,body{width:1200px;height:559px;overflow:hidden;background:var(--page-bg)}
body{font-family:"Source Sans 3",Arial,sans-serif;color:var(--ink)}
.stage{position:relative;width:1268px;height:591px;transform:scale(.94637);transform-origin:0 0}
.abs{position:absolute}

.topbar{left:0;top:0;width:1268px;height:43px;background:linear-gradient(var(--bar-top),var(--bar-bottom));border-bottom:1px solid #2f4779}
.site-mark{left:153px;top:10px;width:22px;height:22px;background:#fff;border-radius:2px}
.search{left:185px;top:9px;width:580px;height:24px;background:#fff;border:1px solid #2f4779;border-radius:2px}
.search svg{position:absolute;right:6px;top:4px}
.nav-icons{left:895px;top:10px;display:flex;gap:8px}
.nav-links{left:998px;top:13px;display:flex;gap:15px;font-size:12px;font-weight:700;color:var(--bar-text)}
.nav-tools{left:1093px;top:13px;display:flex;gap:10px}

.main{left:152px;top:43px;width:851px;height:501px;background:var(--card);border:1px solid var(--card-line);border-top:none}
.cover{left:0;top:0;width:850px;height:312px;background:linear-gradient(110deg,#2d3345 0%,#7c8698 30%,#d9dee5 52%,#bfc6cf 70%,#23262b 100%)}
.cover-copy{left:465px;top:38px;display:flex;flex-direction:column;gap:10px;align-items:flex-start}
.cover-copy span{background:#fff;color:var(--accent);font-size:44px;line-height:51px;padding:0 12px 0 4px}

.profile{left:23px;top:209px;width:170px;height:170px;background:#fff;border:1px solid #9ea3ad;border-radius:3px;display:flex;align-items:center;justify-content:center}
.profile .name{color:var(--brand);font-weight:700;font-size:18px}

.btn{top:331px;height:25px;border:1px solid #9ea3ad;border-radius:2px;background:linear-gradient(#fafbfc,#e8eaef);font-size:13px;font-weight:700;color:#333;display:flex;align-items:center;padding:0 8px;gap:5px}
.btn-liked{left:629px;width:70px}
.btn-message{left:708px;width:118px;padding-right:0}
.btn-message .gear{margin-left:auto;border-left:1px solid #c5c8cf;height:100%;width:42px;display:flex;align-items:center;justify-content:center;gap:4px}

.info{left:1px;top:390px;width:327px;height:74px;background:var(--panel);border:1px solid #e0e3ec;padding:6px 25px;font-size:11px;line-height:16px}
.info .category{color:var(--muted)}
.info a{color:var(--link);text-decoration:none}
.about{left:44px;top:466px;font-size:11px;color:var(--link)}

.tile{top:390px;width:111px;height:74px;background:var(--tile);display:flex;align-items:center;justify-content:center;color:var(--tile-num);font-size:42px}
.tile-likes{background:var(--panel);border:1px solid #dfe2ea;color:#1d2f5c;font-size:22px;font-weight:700;gap:6px}
.tile-likes i{width:20px;height:18px;background:#6c84b8;border-radius:2px;display:block}
.tile-more{left:813px;top:390px;width:37px;height:74px;background:var(--panel);border:1px solid #dfe2ea}
.more{left:810px;top:419px;width:28px;height:16px;background:#fff;border:1px solid #9ea3ad;font-size:11px;display:flex;align-items:center;justify-content:center;gap:3px}
.tile-label{top:471px;font-size:11px;color:var(--link)}

.spine{left:577px;top:544px;width:2px;height:47px;background:#c8cfe0}
.highlights{left:535px;top:561px;width:86px;height:22px;background:#f4f5f9;border:1px solid #c1c7d6;border-radius:2px;font-size:12px;color:#8a93ab;display:flex;align-items:center;justify-content:center;gap:5px}

.years{left:1015px;top:46px;width:60px;list-style:none;border-left:4px solid var(--rail)}
.years li{height:23px;line-height:22px;padding-left:7px;font-size:11px;color:#8994b3}
.years li.active{color:var(--rail-active);font-weight:700;margin-left:-4px;border-left:4px solid var(--rail-active)}
</style>
</head>
<body>
<div class="stage">

  <header class="topbar abs">
    <div class="site-mark abs" aria-label="Friendspace"></div>
    <div class="search abs">
      <svg width="14" height="14" viewBox="0 0 14 14"><circle cx="6" cy="6" r="4.5" fill="none" stroke="#777" stroke-width="1.5"/><line x1="9.3" y1="9.3" x2="13" y2="13" stroke="#777" stroke-width="1.5"/></svg>
    </div>
    <div class="nav-icons abs">
      <svg width="22" height="20" viewBox="0 0 22 20"><circle cx="8" cy="6" r="4" fill="#2c4577"/><path d="M1 18c0-5 14-5 14 0z" fill="#2c4577"/><circle cx="15" cy="7" r="3.5" fill="#2c4577"/></svg>
      <svg width="26" height="20" viewBox="0 0 26 20"><rect x="2" y="3" width="15" height="10" rx="1" fill="#2c4577"/><rect x="9" y="7" width="15" height="10" rx="1" fill="#2c4577"/></svg>
      <svg width="20" height="20" viewBox="0 0 20 20"><circle cx="10" cy="10" r="9" fill="#2c4577"/></svg>
    </div>
    <nav class="nav-links abs"><span>Home</span><span>Evan</span></nav>
    <div class="nav-tools abs">
      <svg width="16" height="14" viewBox="0 0 16 14"><rect x="1" y="5" width="6" height="8" fill="#dfe5f2"/><rect x="9" y="4" width="6" height="2" fill="#dfe5f2"/><rect x="9" y="8" width="6" height="2" fill="#dfe5f2"/></svg>
      <svg width="14" height="14" viewBox="0 0 14 14"><circle cx="7" cy="7" r="4" fill="none" stroke="#dfe5f2" stroke-width="3" stroke-dasharray="2 1.2"/><circle cx="7" cy="7" r="1.5" fill="#dfe5f2"/></svg>
    </div>
  </header>

  <main class="main abs">
    <div class="cover abs" role="img" aria-label="Photo of two business people shaking hands over a desk with a laptop"></div>
    <div class="cover-copy abs">
      <span>Recruit Wisely</span>
      <span>Grow Teams</span>
      <span>Reach Goals</span>
    </div>

    <div class="profile abs">
      <span class="name">TimberLineMetrics</span>
    </div>

    <div class="btn btn-liked abs">
      <svg width="10" height="8" viewBox="0 0 10 8"><path d="M1 4l3 3 5-6" fill="none" stroke="#555" stroke-width="2"/></svg>Liked
    </div>
    <div class="btn btn-message abs">Message
      <span class="gear">
        <svg width="10" height="10" viewBox="0 0 10 10"><circle cx="5" cy="5" r="3" fill="none" stroke="#444" stroke-width="2.5" stroke-dasharray="1.5 1"/></svg>
        <svg width="8" height="5" viewBox="0 0 8 5"><path d="M0 0h8L4 5z" fill="#555"/></svg>
      </span>
    </div>

    <div class="info abs">
      <p class="category">Product/Service</p>
      <p>Our product is awesome... Try it</p>
      <a href="#">http://greatitem.net/</a>
    </div>
    <p class="about abs">About – Suggest an Edit</p>

    <div class="tile abs" style="left:336px">1</div>
    <div class="tile abs" style="left:455px">2</div>
    <div class="tile tile-likes abs" style="left:574px"><i></i>21m</div>
    <div class="tile abs" style="left:693px">4</div>
    <div class="tile-more abs"></div>
    <div class="more abs">3<svg width="7" height="4" viewBox="0 0 7 4"><path d="M0 0h7L3.5 4z" fill="#5b6fa3"/></svg></div>

    <span class="tile-label abs" style="left:336px">Photos</span>
    <span class="tile-label abs" style="left:455px">Videos</span>
    <span class="tile-label abs" style="left:574px">Likes</span>
    <span class="tile-label abs" style="left:693px">Events</span>
  </main>

  <div class="spine abs"></div>
  <div class="highlights abs">Highlights<svg width="7" height="4" viewBox="0 0 7 4"><path d="M0 0h7L3.5 4z" fill="#8a93ab"/></svg></div>

  <ul class="years abs">
    <li class="active">Recent</li>
    <li>2013</li><li>2012</li><li>2011</li><li>2010</li><li>2009</li><li>2008</li>
    <li>2006</li><li>2004</li><li>2003</li><li>2001</li><li>2000</li><li>1998</li>
    <li>1997</li><li>1996</li><li>1995</li><li>1992</li><li>1997</li><li>1988</li>
    <li>1987</li><li>1984</li><li>1983</li><li>1982</li><li>Opened</li>
  </ul>

</div>
</body>
</html>
```